Spanish Student Needs a Cover for his PhD Dissertation

Hi everyone :) So, I'm a Corneal surgeon currently finishing my PhD, with a dissertation focused on the evaluation of quality of life in patients affected by a disease called Keratoconus. Just so you know, Keratoconus is a condition in which the cornea (the frontal part of the way) gets thin and bulgy and it decreases vision. What I did during my PhD was designing a questionnaire for evaluating quality of life in this kind of patients.
I need to design a hard cover for my dissertation, which is 200 sheets long. I like kind of minimalistic and geometric designs but I am totally open to suggestions. What needs to be in the cover is the name of the dissertation "Diseño, desarrollo y validación de una encuesta para evaluar el compromiso visual y emocional subjetivos en pacientes con Queratocono" and my name, "Iñigo Zabaleta". The other thing that needs to go there is the logo of my university (Universidad de Montealto). Aside from that, anything else is up to the designer. It would be important to use the kind of "red" color I am using in the dissertation. I am attaching the frontal page of my dissertation so you know what kind of design and colors I am using.
In the back part, of the cover, there should be this small inscription: "Iñigo Zabaleta, MD, es un Oftalmólogo Subespecialista en Cirugía Refractiva de la Universidad Católica Mirandina (Colombia) y la Universidad de Montealto (España). Actualmente se desempeña como miembro del Departamento de Córnea y Cirugía Refractiva de la Clínica de Oftalmología Los Robles y como director de su propia compañía de emprendimiento médico Silver Heron Surgical". Please leave a space to place my picture; I will have it taken this week so I don't have it right now, you can just leave the blank spot and I will include it later
The size of the pages is standard "letter" size.
Thanks a lot!

Target Market(s)

PhD Scholars

Font styles to use
Serif

Requirements
Must have
• The "red" color I use on my font. It must be formal but "young".
Nice to have
• I like to keep the design clean, kind of "formal with a young" touch so to speak. I really like gray colors, so it would be nice to have broad areas of gray. I love geometrical designs.
I have uploaded a very early version a friend of mine made (it even had a different title); this can be a starting point for you to work on, but I am more than open to suggestions and new ideas.
Should not have
• Please don't use my whole name, Iñigo Zabaleta is fine. I don't like ALL CAPITALS.

```html
<!DOCTYPE html>
<html lang="es">
<head>
<meta charset="utf-8">
<title>Cubierta de tesis doctoral – Iñigo Zabaleta</title>
<link href="https://fonts.googleapis.com/css2?family=Libre+Baskerville:wght@400;700&family=Merriweather:wght@400;700&display=swap" rel="stylesheet">
<style>
  :root{
    --backdrop:#cfd1d0;
    --thesis-red:#a8233b;
    --paper:#ffffff;
    --mist:#eceded;
    --ink:#2b2b2b;
    --placeholder:#e6e6e8;
    --placeholder-text:#a9a9ad;
  }
  *{margin:0;padding:0;box-sizing:border-box}
  html,body{width:909px;height:1200px;overflow:hidden;background:var(--backdrop)}
  .spread{position:absolute;left:25px;top:310px;width:858px;height:580px}
  .panel{position:absolute;top:0;height:580px;overflow:hidden}

  /* Back cover */
  .back{left:0;width:387px;background:var(--paper);font-family:"Merriweather",serif;text-align:center}
  .brand-row{position:absolute;top:72px;left:0;width:100%;display:flex;justify-content:center;gap:26px;align-items:center}
  .brand{display:flex;align-items:center;gap:6px;color:var(--thesis-red);font-size:9.5px;font-weight:700}
  .brand-dot{width:12px;height:12px;border-radius:50%;background:var(--thesis-red)}
  .institution{position:absolute;top:136px;width:100%;font-size:12.5px;line-height:17px}
  .institution .name{color:var(--thesis-red);font-weight:700}
  .institution .program{color:var(--ink)}
  .portrait-slot{position:absolute;left:146px;top:211px;width:96px;height:118px;background:var(--placeholder);display:flex;align-items:center;justify-content:center;color:var(--placeholder-text);font-family:Arial,sans-serif;font-size:15px}
  .bio{position:absolute;top:354px;left:26px;right:26px;color:var(--thesis-red);font-size:10.6px;line-height:15px}
  .bio strong{font-weight:700}
  .credits{position:absolute;top:490px;width:100%;font-size:9.5px;line-height:13px;color:var(--ink)}
  .credits .role{color:var(--thesis-red);font-weight:700}
  .credits p+p{margin-top:3px}
  .credits .gap{margin-top:6px}

  /* Spine */
  .spine{left:397px;width:65px;background:var(--thesis-red);color:var(--paper);font-family:"Libre Baskerville",serif}
  .spine-title{position:absolute;top:66px;left:15px;height:240px;writing-mode:vertical-rl;font-size:7.2px;line-height:10px;text-transform:uppercase}
  .spine-author{position:absolute;top:382px;left:22px;writing-mode:vertical-rl;font-size:16px;font-weight:700;letter-spacing:2px;white-space:nowrap}

  /* Front cover */
  .front{left:472px;width:386px;background:var(--paper);font-family:"Libre Baskerville",serif}
  .facets{position:absolute;inset:190px 0 0 0;background:radial-gradient(ellipse at 60% 65%,var(--paper) 0%,var(--mist) 55%,var(--paper) 100%)}
  .title-band{position:absolute;top:0;left:0;width:100%;height:190px;background:var(--thesis-red);padding:52px 0 0 20px}
  .title{color:var(--paper);font-size:38px;font-weight:400;line-height:47px;letter-spacing:.5px}
  .subtitle{position:absolute;top:214px;left:22px;color:var(--thesis-red);font-size:21.5px;font-weight:400;line-height:29.5px}
  .author{position:absolute;top:503px;width:100%;text-align:center;color:var(--thesis-red);font-size:33px;font-weight:700;word-spacing:10px}
</style>
</head>
<body>
<main class="spread">
  <section class="panel back">
    <div class="brand-row">
      <div class="brand"><span class="brand-dot"></span>Universidad de Montealto</div>
      <div class="brand">Escuela de Doctorado Montealto</div>
    </div>
    <div class="institution">
      <p class="name">Universidad de Montealto</p>
      <p class="name">Instituto Universitario de Ciencias Oculares</p>
      <p class="program">Programa de Doctorado en Ciencias de la Visión</p>
    </div>
    <div class="portrait-slot" role="img" aria-label="Espacio para la fotografía del autor">IMAGE</div>
    <p class="bio"><strong>Iñigo Zabaleta, MD,</strong> es un Oftalmólogo Subespecialista en Cirugía Refractiva de la Universidad Católica Mirandina (Colombia) y la Universidad de Montealto (España). Actualmente se desempeña como miembro del Departamento de Córnea y Cirugía Refractiva de la Clínica de Oftalmología Los Robles y como director de su propia compañía de emprendimiento médico Silver Heron Surgical".</p>
    <div class="credits">
      <p class="role">DIRECTOR:</p>
      <p>Dr. Andrés Felipe Urrutia Salas</p>
      <p class="role gap">TUTOR:</p>
      <p>Dr. Luis Ernesto Villanueva Ocampo</p>
    </div>
  </section>

  <section class="panel spine">
    <p class="spine-title">Diseño, desarrollo y validación de una encuesta para<br>evaluar el compromiso visual y emocional subjetivos en<br>pacientes con queratocono</p>
    <p class="spine-author">IÑIGO ZABALETA</p>
  </section>

  <section class="panel front">
    <div class="facets" role="img" aria-label="Fondo geométrico suave de facetas blancas y grises"></div>
    <div class="title-band">
      <h1 class="title">DISEÑO,<br>DESARROLLO Y<br>VALIDACIÓN</h1>
    </div>
    <h2 class="subtitle">DE UNA ENCUESTA PARA<br>EVALUAR EL COMPROMISO<br>VISUAL Y EMOCIONAL<br>SUBJETIVOS EN PACIENTES<br>CON QUERATOCONO</h2>
    <p class="author">IÑIGO ZABALETA</p>
  </section>
</main>
</body>
</html>
```